business cards

we want our logos on the back
the information on it are on the design I've uploaded
come up with whatever you think is best, we want something professional, sophisticated and sleek.

```html
<!DOCTYPE html>
<html lang="en">
<head>
<meta charset="utf-8">
<title>Keystone – Business Cards</title>
<link href="https://fonts.googleapis.com/css2?family=Montserrat:wght@300;400;700&display=swap" rel="stylesheet">
<style>
  :root {
    --backdrop: #e8e8e9;
    --card: #1d1d1d;
    --ink: #f2f2f2;
    --accent: #22d31c;
    --rule: #d9d9d9;
    --deboss: #121212;
  }
  * { margin: 0; padding: 0; box-sizing: border-box; }
  html, body { width: 1200px; height: 1108px; overflow: hidden; background: var(--backdrop); }
  body { position: relative; font-family: "Montserrat", sans-serif; color: var(--ink); }

  .card { position: absolute; background: var(--card); }
  .card--front { left: 234px; top: 66px; width: 771px; height: 440px; }
  .card--back  { left: 234px; top: 580px; width: 761px; height: 433px; }

  .brand { position: absolute; left: 0; right: 0; text-align: center; }
  .brand__mark { display: block; margin: 0 auto; width: 46px; height: 46px; background: var(--accent); }
  .brand__name {
    display: block; font-weight: 400; letter-spacing: 16px; padding-left: 16px;
  }
  .card--front .brand { top: 72px; }
  .card--front .brand__name { margin-top: 34px; font-size: 40px; color: var(--ink); }

  .card--back .brand { top: 150px; }
  .card--back .brand__mark { width: 70px; height: 70px; background: var(--deboss); }
  .card--back .brand__name { margin-top: 40px; font-size: 56px; letter-spacing: 26px; padding-left: 26px; color: var(--deboss); }

  .person { position: absolute; right: 466px; top: 264px; text-align: right; }
  .person__name { font-weight: 700; font-size: 29px; color: var(--accent); line-height: 1.1; }
  .person__role { font-weight: 400; font-size: 20px; margin-top: 6px; letter-spacing: 0.5px; }

  .divider { position: absolute; left: 330px; top: 264px; width: 1.5px; height: 74px; background: var(--rule); }

  .credentials { position: absolute; left: 345px; top: 258px; font-weight: 400; font-size: 20px; line-height: 30px; }

  .rule { position: absolute; left: 39px; width: 694px; top: 353px; height: 1.5px; background: var(--rule); }

  .contact { position: absolute; display: flex; align-items: center; gap: 10px; font-size: 20px; font-weight: 400; }
  .contact svg { width: 22px; height: 22px; fill: var(--accent); flex: none; }
  .contact--fax   { left: 39px;  top: 372px; }
  .contact--phone { left: 39px;  top: 402px; }
  .contact--email { left: 233px; top: 368px; gap: 12px; }
  .contact--place { left: 238px; top: 402px; gap: 14px; }
</style>
</head>
<body>

<section class="card card--front">
  <div class="brand">
    <span class="brand__mark"></span>
    <span class="brand__name">KEYSTONE</span>
  </div>

  <div class="person">
    <p class="person__name">Daniel Marsh</p>
    <p class="person__role">DIRECTOR</p>
  </div>
  <div class="divider"></div>
  <div class="credentials">
    <p>SENIOR PHYSIOTHERAPIST</p>
    <p>BhlthSc, MPhysioPrac, MExSc(S&amp;C)</p>
    <p>ASCS Level 2</p>
  </div>

  <div class="rule"></div>

  <p class="contact contact--fax">
    <svg viewBox="0 0 24 24" aria-hidden="true"><rect x="3" y="8" width="5" height="14" rx="1"/><rect x="9" y="3" width="12" height="19" rx="1"/><rect x="11" y="5" width="8" height="4" fill="#1d1d1d"/><rect x="11" y="12" width="2" height="2" fill="#1d1d1d"/><rect x="15" y="12" width="2" height="2" fill="#1d1d1d"/><rect x="11" y="16" width="2" height="2" fill="#1d1d1d"/><rect x="15" y="16" width="2" height="2" fill="#1d1d1d"/></svg>
    03 9000 1842
  </p>
  <p class="contact contact--phone">
    <svg viewBox="0 0 24 24" aria-hidden="true"><path d="M6.6 10.8a15.2 15.2 0 0 0 6.6 6.6l2.2-2.2a1 1 0 0 1 1-.25 11.4 11.4 0 0 0 3.6.57 1 1 0 0 1 1 1V20a1 1 0 0 1-1 1A17 17 0 0 1 3 4a1 1 0 0 1 1-1h3.5a1 1 0 0 1 1 1c0 1.25.2 2.45.57 3.57a1 1 0 0 1-.25 1z"/></svg>
    03 9000 2957
  </p>
  <p class="contact contact--email">
    <svg viewBox="0 0 24 24" aria-hidden="true"><path d="M2 5h20v14H2z"/><path d="M2 5l10 8 10-8" fill="none" stroke="#1d1d1d" stroke-width="2"/></svg>
    dan@keystonehealthperform.com.au
  </p>
  <p class="contact contact--place">
    <svg viewBox="0 0 24 24" aria-hidden="true"><path d="M12 2a7 7 0 0 0-7 7c0 5 7 13 7 13s7-8 7-13a7 7 0 0 0-7-7zm0 9.5A2.5 2.5 0 1 1 12 6.5a2.5 2.5 0 0 1 0 5z"/></svg>
    17 Linden St, Northvale
  </p>
</section>

<section class="card card--back">
  <div class="brand">
    <span class="brand__mark"></span>
    <span class="brand__name">KEYSTONE</span>
  </div>
</section>

</body>
</html>
```